Business Card and Stationary for Scuba Dive Company and UW Photography
Deep Reef Co
Modern
Capt. Dan Hollis
CEO
4810 Harbor Ct
Kelport ME 34512
capt.dan@deeprfco.com
www.deeprfco.com
Master Captain, QDTA IDC Staff Instructor
Would also like another card for:
Greta Wenslow
greta@deeprfco.com
Company is focused on Scuba Diving Trips, Travel and Underwater Photography. Will be selling our photos and canvas. Will focus on dive charters and trips specializing in underwater photography.

```html
<!DOCTYPE html>
<html lang="en">
<head>
<meta charset="utf-8">
<title>Deep Reef Co – Stationery</title>
<link rel="stylesheet" href="https://fonts.googleapis.com/css2?family=Raleway:wght@400;500;600&display=swap">
<style>
  :root {
    --page: #ffffff;
    --paper: #ffffff;
    --ink: #1b3f73;
    --deep: #0b2f66;
    --mid: #1c5ea8;
    --glow: #8fd0f2;
    --edge: #c9ced6;
    --on-deep: #eaf4fc;
  }
  * { box-sizing: border-box; margin: 0; padding: 0; }
  html, body { width: 1200px; height: 778px; overflow: hidden; background: var(--page); }
  body { position: relative; font-family: "Raleway", Arial, sans-serif; color: var(--ink); }

  .sheet {
    position: absolute; background: var(--paper);
    border: 1px solid var(--edge);
    box-shadow: 3px 4px 8px rgba(0,0,0,.22);
    overflow: hidden;
  }
  .brand-name {
    font-family: "Raleway", Arial, sans-serif;
    font-weight: 500; color: var(--ink);
    letter-spacing: .04em; white-space: nowrap;
  }
  .ocean {
    position: absolute;
    background:
      radial-gradient(ellipse at 50% 0%, rgba(143,208,242,.75) 0%, rgba(143,208,242,0) 55%),
      linear-gradient(180deg, var(--mid) 0%, var(--deep) 100%);
  }

  /* Letterhead */
  .letterhead { left: 24px; top: 34px; width: 535px; height: 710px; }
  .letterhead .brand-name { position: absolute; top: 48px; left: 0; width: 100%; text-align: center; font-size: 30px; }
  .letterhead .footer-band { left: 0; right: 0; bottom: 22px; height: 34px;
    background: linear-gradient(90deg, var(--deep) 0%, var(--mid) 50%, var(--deep) 100%); }
  .letterhead .footer-line { position: absolute; left: 0; right: 0; bottom: 31px; text-align: center;
    font-size: 11px; color: var(--on-deep); letter-spacing: .03em; white-space: nowrap; }
  .letterhead .footer-web { position: absolute; left: 0; right: 0; bottom: 5px; text-align: center;
    font-size: 11px; color: var(--ink); }

  /* Business card */
  .card { left: 703px; top: 12px; width: 331px; height: 161px; border: none; }
  .card .ocean { inset: 0; }
  .card .brand-name { position: absolute; top: 20px; left: 0; width: 100%; text-align: center;
    font-size: 22px; color: var(--on-deep); }
  .card .details { position: absolute; top: 80px; left: 18px; right: 18px;
    display: flex; justify-content: space-between; font-size: 8.5px; line-height: 1.45; color: var(--on-deep); }
  .card .details .right { text-align: right; }
  .card .holder { font-weight: 600; }
  .card .tagline { position: absolute; left: 0; right: 0; bottom: 9px; text-align: center;
    font-size: 7.5px; color: var(--on-deep); white-space: nowrap; }

  /* Envelope front */
  .envelope-front { left: 595px; top: 252px; width: 574px; height: 235px; }
  .envelope-front .brand-name { position: absolute; top: 26px; left: 22px; font-size: 24px; }

  /* Envelope back */
  .envelope-back { left: 595px; top: 511px; width: 574px; height: 226px; }
  .envelope-back .ocean { left: 0; right: 0; top: 0; height: 48px; }
</style>
</head>
<body>

  <section class="sheet letterhead">
    <div class="brand-name">Deep Reef Co</div>
    <div class="ocean footer-band" role="img" aria-label="Deep blue underwater band"></div>
    <p class="footer-line">4810 Harbor Ct &nbsp;Kelport ME 34512 &nbsp;|&nbsp; Cell - 555-213-0142 &nbsp;|&nbsp; capt.dan@deeprfco.com</p>
    <p class="footer-web">www.deeprfco.com</p>
  </section>

  <section class="sheet card">
    <div class="ocean" role="img" aria-label="Underwater scene with sunlight rays through blue water"></div>
    <div class="brand-name">Deep Reef Co</div>
    <div class="details">
      <div class="left">
        <div class="holder">Capt. Dan Hollis</div>
        <div>CEO, Master Captain</div>
        <div>QDTA IDC Staff Instructor</div>
        <div>capt.dan@deeprfco.com</div>
      </div>
      <div class="right">
        <div>4810 Harbor Ct</div>
        <div>Kelport ME 34512</div>
        <div>Cell - 555-213-0142</div>
        <div>www.deeprfco.com</div>
      </div>
    </div>
    <p class="tagline">Specializing in Dive Charters, Scuba Diving Trips and Underwater Photography</p>
  </section>

  <section class="sheet envelope-front">
    <div class="brand-name">Deep Reef Co</div>
  </section>

  <section class="sheet envelope-back">
    <div class="ocean" role="img" aria-label="Underwater light rays on the envelope flap"></div>
  </section>

</body>
</html>
```